Bluegate Lending Template Design

We need a corporate letterhead template (word) and slide show template (PowerPoint) designed for our Motor Vehicle finance business.

Bluegate Lending provides motor vehicle finance to the credit impaired. Please feel free to visit our website www.bluegatelending.com

Both templates (word and PowerPoint) must include the Bluegate logo (attached to this project) and can be very similar in design.

We are after something creative yet professional in design.

Please feel free to ask any questions.

Thank you
Marlene

```html
<!DOCTYPE html>
<html lang="en">
<head>
<meta charset="utf-8">
<title>Bluegate Lending – Presentation Template</title>
<link href="https://fonts.googleapis.com/css2?family=Montserrat:wght@600;700&family=Questrial&display=swap" rel="stylesheet">
<style>
:root{
  --green:#2fa834;
  --green-dark:#1f8a26;
  --green-light:#7fd77f;
  --grey:#7a7a7a;
  --grey-light:#d6d6d6;
  --ink:#222;
  --white:#fff;
  --page:#fff;
}
*{box-sizing:border-box;margin:0;padding:0}
html,body{width:1200px;height:630px;overflow:hidden;background:var(--page)}
.canvas{position:relative;width:1200px;height:630px}
.slide{position:absolute;width:360px;height:253px;background:var(--white);border:1px solid var(--grey-light);overflow:hidden;font-family:"Questrial",sans-serif;color:var(--ink)}
.slide svg.frame{position:absolute;inset:0;width:100%;height:100%}
.brand{position:absolute;display:flex;align-items:center;gap:5px;font-family:"Montserrat",sans-serif;font-weight:700;color:var(--green);white-space:nowrap}
.brand .mark{display:block;background:var(--grey)}
.brand--large{font-size:15px}
.brand--large .mark{width:26px;height:26px}
.brand--small{font-size:8px;right:14px;bottom:14px}
.brand--small .mark{width:13px;height:13px}
.slide-title{position:absolute;top:22px;right:16px;font-family:"Montserrat",sans-serif;font-weight:700;font-size:14px;color:var(--green);letter-spacing:.5px}
.hero-title{position:absolute;left:24px;font-family:"Montserrat",sans-serif;font-weight:700;font-size:31px;color:var(--white);border-bottom:2px solid var(--white);line-height:1.15;padding-bottom:1px}
.hero-sub{position:absolute;left:24px;color:var(--white);font-size:13px;line-height:1.25}
.body{font-size:6.3px;line-height:1.35;color:var(--ink)}
.block{position:absolute;background:var(--green)}
.point{position:absolute;left:18px;width:130px}
.point h3{font-family:"Montserrat",sans-serif;font-weight:700;font-size:9px;color:var(--green);display:flex;align-items:center;gap:4px;margin-bottom:2px}
.point h3::before{content:"";width:7px;height:7px;background:var(--green)}
.point p{padding-left:11px}
.chart{position:absolute}
.chart text{font-family:"Questrial",sans-serif;fill:var(--ink)}
</style>
</head>
<body>
<main class="canvas">

  <!-- Title slide -->
  <section class="slide" style="left:29px;top:38px">
    <svg class="frame" viewBox="0 0 360 253" preserveAspectRatio="none">
      <polygon points="0,110 296,110 360,6 360,236 0,236" fill="var(--green)"/>
      <rect x="0" y="242" width="360" height="2" fill="var(--grey-light)"/>
    </svg>
    <div class="brand brand--large" style="left:10px;top:14px"><span class="mark"></span>BLUEGATE LENDING</div>
    <h1 class="hero-title" style="top:122px">Welcome</h1>
    <p class="hero-sub" style="top:164px">Presentation Name</p>
  </section>

  <!-- About us -->
  <section class="slide" style="left:419px;top:38px">
    <svg class="frame" viewBox="0 0 360 253" preserveAspectRatio="none">
      <polygon points="0,0 330,0 312,14 0,14" fill="var(--grey)"/>
      <polygon points="330,0 360,0 360,4 340,18 312,14" fill="var(--green)"/>
      <polygon points="150,253 360,232 360,253" fill="var(--green)"/>
      <rect x="0" y="247" width="360" height="2" fill="var(--grey-light)"/>
    </svg>
    <h2 class="slide-title">ABOUT US</h2>
    <div class="block" style="left:18px;top:62px;width:118px;height:103px"></div>
    <div class="body" style="position:absolute;left:178px;top:78px;width:162px">
      <p>The Bluegate Lending Pty Ltd proposition is born out of Australia's credit reporting system.</p><br>
      <p>Traditionally, financial institutions are not willing to deviate from long held lending guidelines which require a perfect credit record. With many more lending institutions having access to the credit reporting system, the system is becoming more and more inequitable.</p><br>
      <p>Bluegate Lending has developed an underwriting strategy which rates and weights credit impairment to determine what level is acceptable credit impairment and what level is unacceptable.</p>
    </div>
    <div class="brand brand--small"><span class="mark"></span>BLUEGATE LENDING</div>
  </section>

  <!-- Three columns -->
  <section class="slide" style="left:809px;top:38px">
    <svg class="frame" viewBox="0 0 360 253" preserveAspectRatio="none">
      <polygon points="0,0 330,0 312,14 0,14" fill="var(--grey)"/>
      <polygon points="330,0 360,0 360,4 340,18 312,14" fill="var(--green)"/>
      <polygon points="150,253 360,232 360,253" fill="var(--green)"/>
      <rect x="0" y="247" width="360" height="2" fill="var(--grey-light)"/>
    </svg>
    <h2 class="slide-title">LOREM IPSUM</h2>
    <div class="block" style="left:18px;top:62px;width:104px;height:58px"></div>
    <div class="block" style="left:128px;top:62px;width:104px;height:58px"></div>
    <div class="block" style="left:238px;top:62px;width:104px;height:58px"></div>
    <p class="body" style="position:absolute;left:22px;top:128px;width:96px">Lorem ipsum dolor sit amet, consectetuer adipiscing elit, sed diam nonummy nibh euismod tincidunt ut laoreet dolore magna aliquam erat volutpat. Ut wisi enim ad minim veniam, quis nostrud exerci tation ullamcorper suscipit lobortis nisl ut aliquip ex ea commodo consequat.</p>
    <p class="body" style="position:absolute;left:132px;top:128px;width:96px">Lorem ipsum dolor sit amet, consectetuer adipiscing elit, sed diam nonummy nibh euismod tincidunt ut laoreet dolore magna aliquam erat volutpat. Ut wisi enim ad minim veniam, quis nostrud exerci tation ullamcorper suscipit lobortis nisl ut aliquip ex ea commodo consequat.</p>
    <p class="body" style="position:absolute;left:242px;top:128px;width:96px">Lorem ipsum dolor sit amet, consectetuer adipiscing elit, sed diam nonummy nibh euismod tincidunt ut laoreet dolore magna aliquam erat volutpat. Ut wisi enim ad minim veniam, quis nostrud exerci tation ullamcorper suscipit lobortis nisl ut aliquip ex ea commodo consequat.</p>
    <div class="brand brand--small"><span class="mark"></span>BLUEGATE LENDING</div>
  </section>

  <!-- Pie chart -->
  <section class="slide" style="left:29px;top:324px">
    <svg class="frame" viewBox="0 0 360 253" preserveAspectRatio="none">
      <polygon points="0,0 330,0 312,14 0,14" fill="var(--grey)"/>
      <polygon points="330,0 360,0 360,4 340,18 312,14" fill="var(--green)"/>
      <polygon points="150,253 360,232 360,253" fill="var(--green)"/>
      <rect x="0" y="247" width="360" height="2" fill="var(--grey-light)"/>
    </svg>
    <h2 class="slide-title">LOREM IPSUM</h2>
    <div class="point body" style="top:76px"><h3>Lorem Ipsum</h3><p>Lorem ipsum dolor sit amet, consectetuer adipiscing elit, sed diam nonummy nibh euismod tincidunt</p></div>
    <div class="point body" style="top:126px"><h3>Lorem Ipsum</h3><p>Lorem ipsum dolor sit amet, consectetuer adipiscing elit, sed diam nonummy nibh euismod tincidunt</p></div>
    <div class="point body" style="top:174px"><h3>Lorem Ipsum</h3><p>Lorem ipsum dolor sit amet, consectetuer adipiscing elit, sed diam nonummy nibh euismod tincidunt</p></div>
    <svg class="chart" style="left:158px;top:62px" width="190" height="130" viewBox="0 0 190 130">
      <path d="M118 70 L118 20 A72 42 0 1 1 70 104 Z" fill="var(--green-dark)"/>
      <path d="M104 66 L56 98 A72 42 0 0 1 60 40 Z" fill="var(--green)"/>
      <path d="M106 58 L66 34 A72 42 0 0 1 88 22 Z" fill="#4cc24f"/>
      <path d="M112 56 L96 18 A72 42 0 0 1 110 16 Z" fill="var(--green-light)"/>
    </svg>
    <div class="brand brand--small"><span class="mark"></span>BLUEGATE LENDING</div>
  </section>

  <!-- Bar chart -->
  <section class="slide" style="left:419px;top:324px">
    <svg class="frame" viewBox="0 0 360 253" preserveAspectRatio="none">
      <polygon points="0,0 330,0 312,14 0,14" fill="var(--grey)"/>
      <polygon points="330,0 360,0 360,4 340,18 312,14" fill="var(--green)"/>
      <polygon points="150,253 360,232 360,253" fill="var(--green)"/>
      <rect x="0" y="247" width="360" height="2" fill="var(--grey-light)"/>
    </svg>
    <h2 class="slide-title">LOREM IPSUM</h2>
    <div class="point body" style="top:62px"><h3>Lorem Ipsum</h3><p>Lorem ipsum dolor sit amet, consectetuer adipiscing elit, sed diam nonummy nibh euismod tincidunt</p></div>
    <div class="point body" style="top:110px"><h3>Lorem Ipsum</h3><p>Lorem ipsum dolor sit amet, consectetuer adipiscing elit, sed diam nonummy nibh euismod tincidunt</p></div>
    <div class="point body" style="top:156px"><h3>Lorem Ipsum</h3><p>Lorem ipsum dolor sit amet, consectetuer adipiscing elit, sed diam nonummy nibh euismod tincidunt</p></div>
    <svg class="chart" style="left:160px;top:70px" width="190" height="110" viewBox="0 0 190 110" font-size="6">
      <g stroke="var(--grey-light)" stroke-width=".6">
        <line x1="14" y1="8" x2="150" y2="8"/><line x1="14" y1="26" x2="150" y2="26"/>
        <line x1="14" y1="44" x2="150" y2="44"/><line x1="14" y1="62" x2="150" y2="62"/>
        <line x1="14" y1="80" x2="150" y2="80"/>
      </g>
      <line x1="14" y1="98" x2="150" y2="98" stroke="var(--grey)" stroke-width=".8"/>
      <line x1="14" y1="8" x2="14" y2="98" stroke="var(--grey)" stroke-width=".8"/>
      <g text-anchor="end"><text x="11" y="100">0</text><text x="11" y="82">1</text><text x="11" y="64">2</text><text x="11" y="46">3</text><text x="11" y="28">4</text><text x="11" y="10">5</text></g>
      <g fill="#6e6e6e"><rect x="20" y="20.6" width="8" height="77.4"/><rect x="54" y="53" width="8" height="45"/><rect x="88" y="35" width="8" height="63"/><rect x="122" y="17" width="8" height="81"/></g>
      <g fill="#a0a0a0"><rect x="28" y="54.8" width="8" height="43.2"/><rect x="62" y="18.8" width="8" height="79.2"/><rect x="96" y="66.8" width="8" height="31.2"/><rect x="130" y="47.6" width="8" height="50.4"/></g>
      <g fill="#cfcfcf"><rect x="36" y="62" width="8" height="36"/><rect x="70" y="62" width="8" height="36"/><rect x="104" y="44" width="8" height="54"/><rect x="138" y="8" width="8" height="90"/></g>
      <g text-anchor="middle"><text x="32" y="107">Category 1</text><text x="66" y="107">Category 2</text><text x="100" y="107">Category 3</text><text x="134" y="107">Category 4</text></g>
      <rect x="156" y="36" width="5" height="5" fill="#6e6e6e"/><text x="163" y="40.5">Series 1</text>
      <rect x="156" y="46" width="5" height="5" fill="#a0a0a0"/><text x="163" y="50.5">Series 2</text>
      <rect x="156" y="56" width="5" height="5" fill="#cfcfcf"/><text x="163" y="60.5">Series 3</text>
    </svg>
    <div class="brand brand--small"><span class="mark"></span>BLUEGATE LENDING</div>
  </section>

  <!-- Closing slide -->
  <section class="slide" style="left:809px;top:324px">
    <svg class="frame" viewBox="0 0 360 253" preserveAspectRatio="none">
      <polygon points="0,95 290,95 360,6 360,236 0,236" fill="var(--green)"/>
      <rect x="0" y="242" width="360" height="2" fill="var(--grey-light)"/>
    </svg>
    <div class="brand brand--large" style="left:10px;top:18px"><span class="mark"></span>BLUEGATE LENDING</div>
    <h1 class="hero-title" style="top:112px">Thanks</h1>
    <p class="hero-sub" style="top:156px;font-size:11px">Lorem ipsum dolor sit amet,<br>consectetuer adipiscing elit,<br>sed diam nonummy nibh</p>
  </section>

</main>
</body>
</html>
```